Modified Business card

We have developed a new logo for the business, and want thou to tray and incorporate it into the business card design that you have done for us.

I am going to upload the logo files. We like the simple clean look that you have on the card, so if you can keep the look incorporating the logo.

Industry/Entity Type

Business

```html
<!DOCTYPE html>
<html lang="en">
<head>
<meta charset="utf-8">
<title>Corvane Engineering – Business Card</title>
<link href="https://fonts.googleapis.com/css2?family=Source+Sans+3:wght@400;600;700&display=swap" rel="stylesheet">
<style>
  :root {
    --brand-red: #d02027;
    --ink-grey: #58585a;
    --card-border: #3a3a3a;
    --paper: #ffffff;
  }
  * { margin: 0; padding: 0; box-sizing: border-box; }
  html, body {
    width: 1200px;
    height: 1000px;
    overflow: hidden;
    background: var(--paper);
    font-family: "Source Sans 3", "Myriad Pro", Arial, sans-serif;
  }
  .card {
    position: absolute;
    left: 214px;
    width: 773px;
    height: 441px;
    border: 1.5px solid var(--card-border);
    background: var(--paper);
    overflow: hidden;
  }
  .card--front { top: 46px; }
  .card--back { top: 511px; }

  /* Front */
  .front-band {
    position: absolute;
    left: 0;
    top: 0;
    width: 245px;
    height: 100%;
  }
  .front-wordmark {
    position: absolute;
    left: 290px;
    top: 188px;
    width: 430px;
    text-align: center;
    font-size: 46px;
    font-weight: 700;
    color: var(--ink-grey);
    letter-spacing: 0.5px;
    line-height: 1;
  }

  /* Back */
  .brand-lockup {
    position: absolute;
    left: 35px;
    top: 37px;
    display: flex;
    align-items: center;
    gap: 16px;
  }
  .brand-lockup__square {
    width: 97px;
    height: 97px;
    border-radius: 5px;
    background: var(--brand-red);
  }
  .brand-lockup__name {
    font-size: 40px;
    font-weight: 700;
    color: var(--ink-grey);
    line-height: 1;
  }

  .person {
    position: absolute;
    right: 32px;
    top: 166px;
    text-align: right;
    color: var(--ink-grey);
  }
  .person__name {
    font-size: 31px;
    font-weight: 700;
    line-height: 36px;
  }
  .person__title {
    font-size: 27px;
    font-weight: 400;
    line-height: 36px;
    letter-spacing: 0.2px;
  }

  .contact-lines {
    position: absolute;
    right: 32px;
    top: 276px;
    text-align: right;
    color: var(--ink-grey);
    font-size: 25px;
    font-weight: 600;
    line-height: 35px;
    list-style: none;
  }
  .contact-lines__label { margin-right: 10px; }

  .company-address {
    position: absolute;
    left: 32px;
    top: 284px;
    color: var(--brand-red);
    font-size: 24px;
    font-weight: 700;
    line-height: 34px;
    font-style: normal;
  }
</style>
</head>
<body>

  <section class="card card--front" aria-label="Business card front">
    <svg class="front-band" viewBox="0 0 245 441" aria-hidden="true">
      <path d="M0 0 H245 V405 A36 36 0 0 1 209 441 H0 Z" fill="var(--brand-red)"/>
    </svg>
    <div class="front-wordmark">Corvane Engineering</div>
  </section>

  <section class="card card--back" aria-label="Business card back">
    <div class="brand-lockup">
      <div class="brand-lockup__square" aria-hidden="true"></div>
      <div class="brand-lockup__name">Corvane Engineering</div>
    </div>

    <div class="person">
      <div class="person__name">Daniel Hart</div>
      <div class="person__title">SENIOR PROJECT MANAGER</div>
    </div>

    <address class="company-address">
      PO Box 2286,<br>
      Franschhoek, 7690<br>
      South Africa<br>
      www.corvane.co.za
    </address>

    <ul class="contact-lines">
      <li><span class="contact-lines__label">m</span>+27 (021) 555 0142</li>
      <li><span class="contact-lines__label">d</span>+27 (021) 555 0187</li>
      <li><span class="contact-lines__label">f</span>+27 (021) 555 0193</li>
      <li>dhart@corvane.co.za</li>
    </ul>
  </section>

</body>
</html>
```